Online Prescription Eyeglass Lens Company Needs a Website

*Update new name to ClearPair. Thx

We are eye doctors with a lab that need a website for a new company based in Southern California called ClearPair. We replace old prescription lenses with new ones next day for most lenses. Patients select the lenses and give us the prescription. We then send a box with a prepaid shipping label. Place the frames in the box and drop them in the mail to our lab. We will custom make new lenses, fit them back into your frames and send them back to you. We would like to compete with www.vizora.com and offer affordable lenses for single vision, bifocal, progressive, sunglass lenses at an affordable price with next day shipping.
Updates

Hi Designers, We have a new name called ClearPair. Can we have the website design reflect the new name and we'll pick our favorites. Thx

Update: The new name is OptiNova . I have not made very many changes or feedback to the submissions because we were bidding for a .com. We won and our new name is OptiNova . This is the last name change.. Please have the website reflect the new name and I'll be providing feedback on the websites . ( I have a separate project for the logo people are working on, so don't worry about creating a logo). Look forward to the submissions. Thanks everyone.

Hi, Just leave the name as ClearPair for now. I will narrow down top designs tonight. Thx

Target Market(s)

Anyone that wears prescription or nonprescription glasses or sunglasses that want next day shipping.

Industry/Entity Type

Eyewear

Number of Pages Required

4 page

Font styles to use
Serif

Colors

Designer to choose colors to be used in the design.

Requirements
Must have
• I need a website that can compete with https://www.vizora.com/.
• We are different from vizora because we can offer same day service or next day shipping.
• It needs to have website that offers the lenses available listed below.
• Needs to be able to upload a prescription and payment feature.
• Pictures of different types of options with small info about each lens option.
• Template Pricing (just use numbers from $79-$179 for now)
• SINGLE VISION LENSES
• HIGH INDEX LENSES
• READING LENSES
• DIGITAL HD PROGRESSIVE LENSES
• RX & NON-RX SUNGLASSES
• RX & NON-RX POLARIZED SUNGLASSES
• COMPUTER LENSES
• TRANSITION LENSES
• BI-FOCAL LENSES

```html
<!DOCTYPE html>
<html lang="en">
<head>
<meta charset="utf-8">
<title>ClearPair – Our Lenses, Your Specs</title>
<link rel="stylesheet" href="https://fonts.googleapis.com/css2?family=Oswald:wght@400;500&family=Roboto:wght@400;500;700&display=swap">
<style>
:root{
  --green:#7fae3c;
  --blue:#55aee3;
  --ink:#1c1c1c;
  --text:#444;
  --muted:#777;
  --line:#d9d9d9;
  --panel:#ececec;
  --tab:#ededed;
  --white:#fff;
  --link:#3a86c8;
}
*{box-sizing:border-box;margin:0;padding:0}
html,body{width:1200px;height:3141px;overflow:hidden}
body{font-family:"Roboto",sans-serif;color:var(--text);background:var(--white);position:relative}
.abs{position:absolute}

/* header */
.site-header{position:absolute;left:0;top:0;width:1200px;height:95px}
.brand{position:absolute;left:80px;top:26px;display:flex;align-items:center;gap:12px}
.brand-dot{width:40px;height:40px;border-radius:50%;background:var(--green)}
.brand-name{font-size:26px;font-weight:700;color:var(--link)}
.main-nav{position:absolute;right:80px;top:36px;font-size:16px;color:var(--ink);display:flex;gap:12px}
.main-nav .active{color:var(--link);font-weight:500}
.main-nav .sep{color:#999}

/* hero */
.hero{position:absolute;top:95px;left:0;width:1200px;height:527px;background:linear-gradient(90deg,#e9eef1 0%,#dfe6ea 45%,#c9d3d9 70%,#b8c4cb 100%)}
.hero-photo{position:absolute;right:0;top:0;width:640px;height:527px;background:radial-gradient(ellipse at 45% 55%,#3a2a24 0%,#6c5247 35%,rgba(200,210,215,0) 70%)}
.hero-copy{position:absolute;left:80px;top:140px;color:var(--ink)}
.hero-lead{font-size:34px;font-weight:500;line-height:43px}
.hero-title{font-family:"Oswald",sans-serif;font-size:54px;font-weight:400;margin-top:14px;letter-spacing:.5px}
.hero-price{font-size:24px;font-weight:500;margin-top:16px}
.btn-green{display:inline-block;margin-top:28px;background:var(--green);color:#fff;font-size:15px;padding:12px 24px;border-radius:4px;text-transform:uppercase}

/* section headings */
.section-head{position:absolute;left:0;width:1200px;text-align:center}
.section-head h2{display:inline-flex;align-items:center;gap:22px;font-size:25px;font-weight:500;color:var(--ink)}
.section-head h2::before,.section-head h2::after{content:"";width:150px;height:6px;background:repeating-linear-gradient(120deg,#555 0 1px,transparent 1px 4px)}
.section-head p{font-size:13px;color:var(--muted);margin-top:12px}

/* steps */
.steps{position:absolute;top:738px;left:0;width:1200px;height:237px;overflow:hidden}
.step{position:absolute;top:0;height:237px;width:442px;color:#fff;text-align:center}
.step.green{background:var(--green)}
.step.blue{background:var(--blue)}
.step-num{font-size:40px;margin-top:32px;font-weight:400}
.step h3{font-size:22px;font-weight:500;margin-top:12px}
.step p{font-size:13px;font-weight:500;line-height:18px;margin:14px auto 0;width:210px}
.step-art{position:absolute;left:22px;top:95px;width:130px;height:142px;background:rgba(255,255,255,.35);border-radius:8px 8px 0 0}

/* optical tabs */
.tabs{position:absolute;left:80px;top:1097px;width:315px}
.tab{height:48px;background:var(--tab);margin-bottom:1px;display:flex;align-items:center;gap:12px;padding-left:18px;font-size:15px;color:#666}
.tab.active{background:var(--green);color:#fff}
.tab svg{width:24px;height:12px;flex:none}
.lens-detail{position:absolute;left:420px;top:1097px;width:720px}
.lens-detail h3{font-size:24px;font-weight:500;color:var(--ink);padding-bottom:8px;border-bottom:1px solid #aaa;display:inline-block;padding-right:22px}
.lens-detail p{font-size:15.5px;line-height:27px;color:#333;margin-top:22px}
.features{list-style:none;margin-top:14px}
.features li{font-size:15px;color:#333;height:39px;display:flex;align-items:center;gap:22px;padding-left:10px}
.features li::before{content:"";width:7px;height:7px;border:1.5px solid #777;border-radius:50%}
.product-shot{position:absolute;left:700px;top:1290px;width:410px;height:160px;background:radial-gradient(ellipse,#f4c6c6 0%,#fff 70%)}

/* promo tiles */
.tile{position:absolute;color:#fff;font-family:"Oswald",sans-serif;font-size:36px;line-height:44px;text-transform:uppercase}
.tile span{position:absolute;left:34px;bottom:34px}
.tile-1{left:80px;top:1550px;width:525px;height:224px;background:linear-gradient(90deg,#6b6b6b 0%,#2b2b2b 45%,#111 100%)}
.tile-1 span{left:243px}
.tile-2{left:80px;top:1800px;width:525px;height:220px;background:linear-gradient(180deg,#1a2233 0%,#1f4a66 55%,#0f3450 100%)}
.tile-3{left:630px;top:1550px;width:510px;height:470px;background:linear-gradient(180deg,#8aa1b4 0%,#9c7a62 45%,#3b2a21 100%)}

/* subscribe + testimonial */
.subscribe{position:absolute;left:0;top:2063px;width:605px;height:230px;background:var(--panel)}
.subscribe h3{position:absolute;left:98px;top:54px;font-size:24px;font-weight:500;color:var(--ink)}
.subscribe .note{position:absolute;left:98px;top:100px;font-size:13px;font-weight:500;color:#333}
.subscribe form{position:absolute;left:98px;top:142px;display:flex}
.subscribe input{width:325px;height:52px;border:0;padding-left:24px;font:14px "Roboto",sans-serif;color:#aaa;background:#fff}
.subscribe button{width:147px;height:52px;border:0;background:var(--green);color:#fff;font:500 20px "Roboto",sans-serif}
.subscribe .edge{position:absolute;left:0;top:130px;width:12px;height:70px;background:#2f2f2f;border-radius:0 8px 8px 0}
.testimonial{position:absolute;left:630px;top:2063px;width:570px;height:230px;background:var(--panel)}
.avatar{position:absolute;left:35px;top:63px;width:110px;height:110px;border-radius:50%;border:4px solid var(--blue);background:linear-gradient(180deg,#4a3a36,#c9a99a)}
.quote-mark{position:absolute;left:143px;top:18px;font-family:"Oswald",sans-serif;font-size:56px;color:#999}
.testimonial blockquote{position:absolute;left:173px;top:52px;width:397px;height:66px;overflow:hidden;white-space:nowrap;font-size:13px;line-height:22px;color:#888}
.testimonial cite{position:absolute;left:173px;top:132px;font-style:normal;font-size:18px;color:var(--ink)}
.testimonial .role{position:absolute;left:173px;top:160px;font-size:12px;color:#999}
.dots{position:absolute;left:173px;top:190px;display:flex;gap:5px}
.dots i{width:9px;height:9px;border-radius:50%;background:var(--blue)}
.dots i.on{background:var(--green)}

/* products */
.product{position:absolute;top:2423px;width:245px;height:305px;border:1px solid var(--line);text-align:center}
.product-img{width:190px;height:110px;margin:46px auto 0;background:radial-gradient(ellipse,#cfd6dc 0%,#fff 70%)}
.product h4{font-size:15px;font-weight:500;color:var(--ink);margin-top:22px}
.price{font-size:14px;color:#666;margin-top:18px;display:flex;justify-content:center;gap:14px}
.price s{color:#999}
.btn-outline{display:inline-block;margin-top:18px;border:1px solid #999;border-radius:3px;font-size:12px;color:#333;padding:5px 24px}

/* footer */
.site-footer{position:absolute;left:0;top:2778px;width:1200px;height:363px;background:var(--panel)}
.footer-rule{position:absolute;top:55px;height:1px;background:#bbb}
.footer-icon{position:absolute;top:38px}
.footer-col{position:absolute;top:82px;font-size:14px;line-height:23px;color:#333}
.footer-brand{position:absolute;left:0;top:150px;width:1200px;display:flex;justify-content:center;align-items:center;gap:12px}
.social{position:absolute;top:225px;left:0;width:1200px;display:flex;justify-content:center;gap:16px}
.social i{width:24px;height:24px;border-radius:50%;background:#555}
.social i.first{background:var(--green)}
.footer-nav{position:absolute;top:275px;left:0;width:1200px;display:flex;justify-content:center;gap:12px;font-size:14px;color:#333}
.footer-nav .active{color:var(--green)}
.copyright{position:absolute;top:310px;left:0;width:1200px;text-align:center;font-size:13px;color:#333}
</style>
</head>
<body>

<header class="site-header">
  <div class="brand"><span class="brand-dot"></span><span class="brand-name">ClearPair</span></div>
  <nav class="main-nav">
    <span class="active">Home</span><span class="sep">/</span><span>About Us</span><span class="sep">/</span><span>What We Do</span><span class="sep">/</span><span>Cotact Leans</span><span class="sep">/</span><span>Blog</span><span class="sep">/</span><span>Contact Us</span>
  </nav>
</header>

<section class="hero">
  <div class="hero-photo" role="img" aria-label="Smiling woman wearing red-framed glasses in an optical store"></div>
  <div class="hero-copy">
    <p class="hero-lead">Get the lenses you need, in your<br>own frames, without leaving home.</p>
    <h1 class="hero-title">OUR LENSES, YOUR SPECS.</h1>
    <p class="hero-price">STARTING AT $77</p>
    <a class="btn-green">Choose your lenses</a>
  </div>
</section>

<div class="section-head" style="top:660px">
  <h2>How ClearPair Works</h2>
  <p>A brief overview of the process that will have your new lenses delivered back at your door in around 2 weeks or less.</p>
</div>

<section class="steps">
  <div class="step green" style="left:-275px">
    <div class="step-num">1</div>
    <h3>Choose Your Lenses</h3>
    <p>Select lens options ®, pick your coating where you need your new lenses.</p>
  </div>
  <div class="step blue" style="left:167px">
    <div class="step-art" role="img" aria-label="Line drawing of eyeglasses"></div>
    <div class="step-num">2</div>
    <h3>Send Us Your Frames.</h3>
    <p>Use the prepaid, secure box we provide to send us your favorite frames.</p>
  </div>
  <div class="step green" style="left:609px">
    <div class="step-art" role="img" aria-label="Line drawing of a technician inspecting a lens"></div>
    <div class="step-num">3</div>
    <h3>We Re Lens Your Glasses</h3>
    <p>We scan your frames, cut new lenses, and fit them perfectly into your frames.</p>
  </div>
  <div class="step blue" style="left:1051px">
    <div class="step-art" role="img" aria-label="Line drawing of a courier delivering a box"></div>
    <div class="step-num">4</div>
    <h3>Sight Restored</h3>
    <p>Sit back while your new lenses are shipped to your door.</p>
  </div>
</section>

<div class="section-head" style="top:1013px">
  <h2>The Perfect Optical</h2>
  <p>A brief overview of the process that will have your new lenses delivered back at your door in around 2 weeks or less.</p>
</div>

<svg width="0" height="0" style="position:absolute">
  <symbol id="glasses" viewBox="0 0 24 12"><circle cx="6" cy="6" r="4.5" fill="none" stroke="currentColor" stroke-width="1.5"/><circle cx="18" cy="6" r="4.5" fill="none" stroke="currentColor" stroke-width="1.5"/><path d="M10.5 5.5q1.5-1.5 3 0" fill="none" stroke="currentColor" stroke-width="1.5"/></symbol>
</svg>
<aside class="tabs">
  <div class="tab active"><svg><use href="#glasses"/></svg>Single Vision Lenses</div>
  <div class="tab"><svg><use href="#glasses"/></svg>High Index Lenses</div>
  <div class="tab"><svg><use href="#glasses"/></svg>Reading Lenses</div>
  <div class="tab"><svg><use href="#glasses"/></svg>Digital HD Progressive Lenses</div>
  <div class="tab"><svg><use href="#glasses"/></svg>Rx &amp; Non Rx Sunglasses</div>
  <div class="tab"><svg><use href="#glasses"/></svg>Rx &amp; Non Rx Polarized Sunglasses</div>
  <div class="tab"><svg><use href="#glasses"/></svg>Computer Lenses</div>
  <div class="tab"><svg><use href="#glasses"/></svg>Transition Lenses</div>
</aside>
<article class="lens-detail">
  <h3>Single Vision Lense</h3>
  <p>These are lenses which have a single power over the whole lens. They would be used, for example, for someone who needs spectacles only for driving or for reading. In some cases, a person's eyes may need lenses to focus at both far and near distances and their prescription ('strength' of the lens they need) is the same for both. In this case they can use the same single vision lens for.</p>
  <ul class="features">
    <li>7-25 days on delivary</li>
    <li>Maion Material: Plastic</li>
    <li>For Hard or Soft lenses</li>
    <li>Coated lids for superior grip</li>
    <li>Leak-proof design</li>
    <li>Package Included</li>
  </ul>
</article>
<div class="product-shot" role="img" aria-label="Red plastic eyeglass frame"></div>

<div class="tile tile-1" role="img" aria-label="Woman wearing dark glasses"><span>Solving<br>Visual Problems</span></div>
<div class="tile tile-2" role="img" aria-label="Man in sunglasses on a sailboat"><span>Spectacles<br>Starting at $77</span></div>
<div class="tile tile-3" role="img" aria-label="Smiling couple wearing sunglasses"><span>Vision Care for our Family</span></div>

<section class="subscribe">
  <span class="edge"></span>
  <h3>SUBSCRIBE EMAIL</h3>
  <p class="note">Majority or which don't look even slightlyable.</p>
  <form><input type="text" value="Your Email Address:" aria-label="Email address"><button type="button">Subscribe</button></form>
</section>
<section class="testimonial">
  <div class="avatar" role="img" aria-label="Customer portrait"></div>
  <span class="quote-mark">“</span>
  <blockquote>Lorem ipsum dolor sit amet, consectetur adipiscing elit. Nunc magna<br>interdum mollis ex. Aliquam in lorem at eros lacinia vehicula ut<br>Nulla in dictum augue. Donec accumsan et nulla in interdum.</blockquote>
  <cite>Lorem Isumn</cite>
  <span class="role">Housewife City Name</span>
  <div class="dots"><i></i><i class="on"></i><i></i></div>
</section>

<div class="section-head" style="top:2330px">
  <h2>Special Products</h2>
  <p>Lorem ipsum dolor sit amet, consectetur adipiscing elit. Nunc magna ex, lacinia vitae nunc eget, interdum mollis ex. Aliquam in lorem at</p>
</div>

<div class="product" style="left:80px"><div class="product-img" role="img" aria-label="Black frame glasses with blue temples"></div><h4>Ridgeway RW9103</h4><div class="price"><s>54,95 €</s><span>Best Price 34,27€</span></div><a class="btn-outline">Shop Now</a></div>
<div class="product" style="left:352px"><div class="product-img" role="img" aria-label="Dark round sunglasses"></div><h4>Flexara SUN FX-5026P</h4><div class="price"><s>89,95 €</s><span>Best Price 84,50 €</span></div><a class="btn-outline">Shop Now</a></div>
<div class="product" style="left:624px"><div class="product-img" role="img" aria-label="Black and red rectangular frame glasses"></div><h4>Harlow HX Chief</h4><div class="price"><s>70,46 €</s><span>Best Price 67,41 €</span></div><a class="btn-outline">Shop Now</a></div>
<div class="product" style="left:895px"><div class="product-img" role="img" aria-label="Blue frame glasses"></div><h4>Marlo Vence Neria/S</h4><div class="price"><s>112,90 €</s><span>Best Price 99,95 €</span></div><a class="btn-outline">Shop Now</a></div>

<footer class="site-footer">
  <div class="footer-rule" style="left:205px;width:380px"></div>
  <div class="footer-rule" style="left:640px;width:375px"></div>
  <svg class="footer-icon" style="left:158px" width="32" height="24" viewBox="0 0 32 24"><rect x="1" y="2" width="30" height="20" fill="var(--green)"/><path d="M1 2l15 11L31 2" fill="none" stroke="#fff" stroke-width="2"/></svg>
  <svg class="footer-icon" style="left:602px" width="26" height="32" viewBox="0 0 26 32"><path d="M13 1a10 10 0 0 0-10 10c0 8 10 17 10 17s10-9 10-17A10 10 0 0 0 13 1z" fill="var(--green)"/><circle cx="13" cy="11" r="4" fill="#fff"/><rect x="2" y="29" width="22" height="2" fill="var(--green)"/></svg>
  <svg class="footer-icon" style="left:1058px" width="28" height="28" viewBox="0 0 28 28"><rect x="2" y="6" width="24" height="20" rx="3" fill="var(--green)"/><rect x="6" y="1" width="16" height="7" rx="3" fill="var(--green)"/><circle cx="14" cy="17" r="5" fill="#fff"/></svg>
  <div class="footer-col" style="left:80px">info@clearpair-mail.com<br>support@clearpair-mail.com</div>
  <div class="footer-col" style="left:400px;width:420px;text-align:center">Lorem ipsum dolor 507, Maximus gravida, Ring<br>bibendum, USA- 1234656</div>
  <div class="footer-col" style="left:990px;text-align:right;width:150px">Call us : 1234-567-890<br>Call us : 0987-654-321</div>
  <div class="footer-brand"><span class="brand-dot"></span><span class="brand-name" style="color:var(--green)">ClearPair</span></div>
  <div class="social" aria-label="Social links"><i class="first"></i><i></i><i></i><i></i><i></i><i></i></div>
  <nav class="footer-nav"><span class="active">Home</span><span>/</span><span>About Us</span><span>/</span><span>What We Do</span><span>/</span><span>Cotact Leans</span><span>/</span><span>Blog</span><span>/</span><span>Contact Us</span></nav>
  <p class="copyright">Copyright © 2017 ClearPair. All rights reserved.</p>
</footer>

</body>
</html>
```